Book Cover Design for a Novella

This book is a whimsical book about random philosophical thoughts. The size of the book is 4X6 inches, about 140 pages long. I would like the background color to be maroon. The title of the book is The Lantern Keeper's Crooked Almanac of Days, and the author name is Delia Marwood. I would like the lettering to either be black or gold, in a font that looks like handwriting. From the lower left corner of the front cover, I would like there to be a gold-colored gardenia.
On the back cover, this is the book summary/description: “We are meant to share our hearts, not give them away. Vulnerability is not the act of placing your heart in someone else’s hands, saying, ‘Keep this safe for me.’ Vulnerability is wearing your heart on your sleeve, showing others your beauty, truths, and fears, and trusting that they will respect you.”
For the author's bio: Delia Marwood is a native of Boulder, Colorado. She enjoys spending time with her cats, eating pasta, and contemplating random things, such as banana spiders, sewage systems, and other huge things that scare her.
I would like all the writing on the back to be in a black, regular font.
I will upload the author's photo, which I would like to be put next to the bio, and I will also attach a rough sketch of what I'd like the cover to look like. Message me with any questions! Thanks.

```html
<!DOCTYPE html>
<html lang="en">
<head>
<meta charset="utf-8">
<title>The Lantern Keeper's Crooked Almanac of Days – Cover</title>
<link href="https://fonts.googleapis.com/css2?family=Damion&family=Niconne&display=swap" rel="stylesheet">
<style>
  :root {
    --maroon: #4c0708;
    --ink: #ffffff;
    --petal: #f3f0e2;
    --petal-shade: #d9d6bd;
    --leaf: #7ea543;
    --leaf-dark: #3f6220;
    --portrait: #b9a48f;
  }
  html, body {
    margin: 0;
    padding: 0;
    overflow: hidden;
    background: var(--maroon);
  }
  .cover {
    position: relative;
    width: 1200px;
    height: 854px;
    background: var(--maroon);
    color: var(--ink);
    overflow: hidden;
  }
  .back-blurb {
    position: absolute;
    left: 0;
    top: 170px;
    width: 492px;
    margin: 0;
    text-align: center;
    font-family: "Damion", cursive;
    font-size: 20px;
    line-height: 30px;
  }
  .author-portrait {
    position: absolute;
    left: 27px;
    top: 642px;
    width: 108px;
    height: 108px;
    border-radius: 50%;
    background: radial-gradient(circle at 50% 40%, #d8c3ad, var(--portrait) 55%, #4a3a32);
    box-shadow: 0 0 0 2px rgba(255,255,255,0.35);
  }
  .author-bio {
    position: absolute;
    right: 679px;
    top: 662px;
    width: 500px;
    margin: 0;
    text-align: right;
    font-family: "Damion", cursive;
    font-size: 17px;
    line-height: 23px;
  }
  .spine-title,
  .spine-author {
    position: absolute;
    writing-mode: vertical-rl;
    font-family: "Damion", cursive;
    white-space: nowrap;
  }
  .spine-title {
    left: 574px;
    top: 36px;
    font-size: 25px;
  }
  .spine-author {
    left: 568px;
    top: 542px;
    font-size: 38px;
  }
  .front-title {
    position: absolute;
    right: 52px;
    top: 62px;
    margin: 0;
    text-align: right;
    font-family: "Niconne", "Damion", cursive;
    font-weight: normal;
    font-size: 66px;
    line-height: 95px;
  }
  .gardenia {
    position: absolute;
    left: 641px;
    top: 516px;
    width: 420px;
    height: 338px;
  }
  .front-author {
    position: absolute;
    right: 28px;
    top: 780px;
    margin: 0;
    font-family: "Niconne", "Damion", cursive;
    font-size: 36px;
  }
</style>
</head>
<body>
<main class="cover">
  <section class="back-cover">
    <p class="back-blurb">“We are meant to share our hearts,<br>
      not give them away. Vulnerability is not the act of<br>
      placing your heart in someone else’s hands,<br>
      saying, ‘Keep this safe for me.’<br>
      Vulnerability is wearing your heart on<br>
      your sleeve, showing others your beauty,<br>
      truths, and fears, and trusting<br>
      that they will respect you.”</p>
    <div class="author-portrait" role="img" aria-label="Author portrait photo"></div>
    <p class="author-bio">Delia Marwood is a native of Boulder,<br>
      Colorado. She enjoys spending time with<br>
      her cats, eating pasta, and contemplating<br>
      random things, such as banana spiders,<br>
      sewage systems, and other huge things that scare her.</p>
  </section>

  <section class="spine">
    <div class="spine-title">The Lantern Keeper's Crooked Almanac of Days</div>
    <div class="spine-author">Delia Marwood</div>
  </section>

  <section class="front-cover">
    <h1 class="front-title">The Lantern<br>Keeper's Crooked<br>Almanac of<br>Days.</h1>
    <svg class="gardenia" viewBox="0 0 420 338" role="img" aria-label="Photograph of a white gardenia bloom among green leaves">
      <defs>
        <radialGradient id="bloomTone" cx="32%" cy="62%" r="70%">
          <stop offset="0" stop-color="var(--petal)"/>
          <stop offset="0.28" stop-color="var(--petal-shade)"/>
          <stop offset="0.5" stop-color="var(--leaf)"/>
          <stop offset="0.78" stop-color="var(--leaf-dark)"/>
          <stop offset="1" stop-color="var(--maroon)"/>
        </radialGradient>
      </defs>
      <rect x="0" y="0" width="420" height="338" fill="url(#bloomTone)"/>
    </svg>
    <p class="front-author">Delia Marwood</p>
  </section>
</main>
</body>
</html>
```